Wordpress Design Project drem.ie

We want to setup a new WP site for a VANTELORE USER group in Ireland. We hae the logo and a short intro video
We want to be able to blog and post videos (clipra links) to the page.

If you look at the image below *drem site this is a try we made, but have run out of time.

Target Market(s)

Techies and mostly bouring men like us.

Industry/Entity Type

Group

Requirements
Must have
• 4 pages, Simple Clean and easy to nivagate and easy for us to use.

Explore
Plan
Deploy
Configure

have a look at - http://www.drem.be/ We do not want an exact copy of
Nice to have
• Login
down load section
link to other blogs etc
social netwrok links LM,Quabble etc
about us

```html
<!DOCTYPE html>
<html lang="en">
<head>
<meta charset="utf-8">
<title>DREM.IE – Fleet Console User Group Ireland</title>
<link rel="stylesheet" href="https://fonts.googleapis.com/css2?family=Ubuntu:wght@400;500&family=Lato:wght@400;700&display=swap">
<style>
:root{
  --green:#5fb336;
  --green-dark:#3f8f1f;
  --ink:#222;
  --body:#333;
  --muted:#666;
  --line:#d8d8d8;
  --dark:#1c1c1c;
  --band-top:#4a4a4a;
  --band-bot:#0f0f0f;
  --white:#fff;
}
*{box-sizing:border-box;margin:0;padding:0}
html,body{width:946px;height:1200px;overflow:hidden;background:var(--white)}
body{position:relative;font-family:'Lato',sans-serif;color:var(--body)}
.abs{position:absolute}

.topbar{left:0;top:0;width:946px;height:26px;background:var(--green);display:flex;justify-content:flex-end;align-items:center;padding-right:36px;font-family:'Ubuntu',sans-serif;font-size:11px;color:var(--white)}
.topbar span{margin:0 8px}

.brand{left:31px;top:55px}
.brand-name{font-family:'Ubuntu',sans-serif;font-size:31px;line-height:30px;color:var(--ink);letter-spacing:.5px}
.brand-sub{font-family:'Ubuntu',sans-serif;font-size:16px;line-height:16px;color:var(--ink)}
.brand-tag{font-family:'Ubuntu',sans-serif;font-size:14px;line-height:15px;color:var(--green)}
.brand-mark{left:170px;top:58px;width:46px;height:46px;background:var(--green)}

.mainnav{top:97px;height:43px;left:455px;display:flex;font-family:'Ubuntu',sans-serif;font-size:13.5px;color:var(--ink)}
.mainnav a{display:flex;align-items:center;padding:0 17px;height:43px;color:inherit;text-decoration:none}
.mainnav a.active{background:linear-gradient(#3a3a3a,#1a1a1a);color:var(--white);padding:0 18px;margin-right:0}

.hero{left:17px;top:140px;width:911px;height:425px;border:1px solid #cfcfcf}
.hero-photo{position:absolute;left:0;top:0;width:909px;height:320px;background:linear-gradient(100deg,#e7e3de 0%,#c9c4bd 30%,#8a8178 50%,#d8d3ce 70%,#bdb6d0 85%,#e8e6ea 100%)}
.hero-pointer{position:absolute;left:98px;top:306px;width:0;height:0;border-left:15px solid transparent;border-right:15px solid transparent;border-bottom:15px solid var(--band-top)}
.hero-band{position:absolute;left:0;top:321px;width:909px;height:103px;display:flex;background:linear-gradient(var(--band-top),var(--band-bot))}
.band-item{flex:1;position:relative;border-right:1px solid #111;box-shadow:inset -1px 0 0 #555}
.band-item:last-child{border-right:none;box-shadow:none}
.band-thumb{position:absolute;left:16px;top:18px;width:80px;height:71px;border:3px solid var(--white)}
.band-title{position:absolute;left:105px;top:24px;font-family:'Ubuntu',sans-serif;font-size:15px;color:var(--white)}
.band-text{position:absolute;left:105px;top:50px;font-family:'Ubuntu',sans-serif;font-size:10.5px;color:#cfcfcf}

.about{left:26px;top:598px;width:620px}
.section-title{font-family:'Ubuntu',sans-serif;font-weight:400;color:var(--green-dark);font-size:19px;margin-bottom:8px}
.lead{font-size:12.5px;line-height:16.5px;color:var(--ink)}
.small{font-size:10.5px;line-height:16.6px;color:var(--body)}
.gap{margin-top:16.6px}

.divider{left:25px;top:818px;width:629px;height:1px;background:var(--line)}

.howwork{left:26px;top:842px}
.sub-title{font-family:'Ubuntu',sans-serif;font-weight:400;font-size:17px;color:var(--ink)}
.video{left:23px;top:870px;width:288px;height:202px;background:#e6e2de;padding:5px}
.video-still{position:relative;width:100%;height:100%;background:linear-gradient(90deg,#cfd6dc 0%,#9aa4ad 35%,#ece8e2 60%,#c9b49a 80%,#efece8 100%)}
.video svg{position:absolute;left:0;top:0}

.whatwedo{left:342px;top:842px;width:305px}
.whatwedo .sub-title{margin-bottom:10px}
.whatwedo .small{text-align:justify}
.learn{font-family:'Ubuntu',sans-serif;font-size:13px;color:var(--ink);margin-top:12px}

.sidebar{left:684px;top:583px;width:243px;height:530px;border:1px solid #e2e2e2;border-top:none}
.side-head{height:36px;background:var(--green);color:var(--white);font-family:'Ubuntu',sans-serif;font-size:17px;display:flex;align-items:center;padding-left:17px}
.login{padding:10px 16px 0 16px}
.login .note{font-size:10px;line-height:16.5px;color:var(--muted);padding-left:2px}
.field-label{font-size:11.5px;color:var(--ink);margin-top:10px;margin-bottom:4px}
.field{height:26px;border:1px solid #d6d6d6;border-radius:3px;background:#fff}
.remember{display:flex;align-items:center;font-size:10.5px;color:var(--muted);margin-top:9px}
.remember i{display:inline-block;width:12px;height:12px;border:1px solid #ccc;margin-right:7px}
.btn{display:inline-block;margin-top:12px;background:#111;color:var(--white);font-family:'Ubuntu',sans-serif;font-size:12px;padding:5px 13px;border-radius:3px;border:1px solid #000}
.blog-links{list-style:none;padding:10px 0 0 20px}
.blog-links li{font-size:11px;color:var(--ink);line-height:25px;display:flex;align-items:center}
.blog-links li::before{content:"";display:inline-block;width:0;height:0;border-top:4px solid transparent;border-bottom:4px solid transparent;border-left:4px solid #333;margin-right:10px}

.footer{left:0;top:1113px;width:946px;height:87px;background:linear-gradient(#353535,var(--dark))}
.foot-nav{position:absolute;left:26px;top:18px;font-family:'Ubuntu',sans-serif;font-size:11px;color:var(--white)}
.foot-nav span{margin:0 6px;color:#bbb}
.copy{position:absolute;left:26px;top:44px;font-size:10px;color:#ccc}
.social{position:absolute;right:28px;top:10px;display:flex;gap:10px}
.social-item{display:flex;align-items:center;gap:5px;font-family:'Ubuntu',sans-serif;font-size:10px;color:var(--white)}
.social-item i{display:block;width:32px;height:32px;border-radius:50%;background:var(--white);border:2px solid #ddd}
</style>
</head>
<body>

<div class="abs topbar"><span>FAQ</span>|<span>Sign In</span>|<span>Log in</span>|<span>Videos</span></div>

<div class="abs brand">
  <div class="brand-name">DREM.IE</div>
  <div class="brand-sub">Fleet Console</div>
  <div class="brand-tag">User Group Ireland</div>
</div>
<div class="abs brand-mark" style="left:172px"></div>

<nav class="abs mainnav">
  <a class="active" href="#">Home</a>
  <a href="#">Features</a>
  <a href="#">Plugins</a>
  <a href="#">Tutorials</a>
  <a href="#">Fltcnsl</a>
  <a href="#">Contact</a>
</nav>

<section class="abs hero">
  <div class="hero-photo" role="img" aria-label="Photo of three colleagues in business attire smiling at a laptop"></div>
  <div class="hero-pointer"></div>
  <div class="hero-band">
    <div class="band-item">
      <div class="band-thumb" role="img" aria-label="Thumbnail photo of a smiling businessman" style="background:linear-gradient(135deg,#d9d2c8,#7d7066)"></div>
      <div class="band-title">Explore</div>
      <div class="band-text">Explore Fleet Console</div>
    </div>
    <div class="band-item">
      <div class="band-thumb" role="img" aria-label="Thumbnail of a planning diagram" style="background:linear-gradient(135deg,#1d3f66,#0b1c33)"></div>
      <div class="band-title">Paln</div>
      <div class="band-text">Plan Fleet Console</div>
    </div>
    <div class="band-item">
      <div class="band-thumb" role="img" aria-label="Thumbnail of a deployment flow chart" style="background:linear-gradient(135deg,#2c6fc2,#154a92)"></div>
      <div class="band-title">Deplay</div>
      <div class="band-text">Deplay Fleet Console</div>
    </div>
    <div class="band-item">
      <div class="band-thumb" role="img" aria-label="Thumbnail of a configuration overview chart" style="background:linear-gradient(135deg,#3a5fb8,#6ea32c 60%,#2f9a6a)"></div>
      <div class="band-title">Configure</div>
      <div class="band-text">Explore Fleet Console</div>
    </div>
  </div>
</section>

<section class="abs about">
  <h2 class="section-title">About Us</h2>
  <p class="lead">Lorem ipsum dolor sit amet, consectetuer adipiscing elit. Nam cursus. Morbi ut mi. Nullam enim leo, egestas id, condimentum at, laoreet mattis, massa. Sed eleifend nonummy diam.</p>
  <p class="small">Praesent mauris ante, elementum et, bibendum at, posuere sit amet, nibh. Duis tincidunt lectus quis dui viverra vestibulum. Suspendisse vulputate aliquam dui.</p>
  <p class="small gap">Nulla elementum dui ut augue. Aliquam vehicula mi at mauris. Maecenas placerat, nisl at consequat rhoncus, sem nunc gravida justo, quis eleifend arcu velit quis lacus. Morbi magna magna, tincidunt a, mattis non, imperdiet vitae, tellus. Sed odio est, auctor ac, sollicitudin in, consequat vitae, orci. Fusce id felis. Vivamus sollicitudin metus eget eros.</p>
  <p class="small">Pellentesque habitant morbi tristique senectus et netus et malesuada fames ac turpis egestas. In posuere felis nec tortor. Pellentesque faucibus. Ut accumsan ultricies elit. Maecenas at justo id velit placerat molestie.</p>
</section>

<div class="abs divider"></div>

<div class="abs howwork"><h3 class="sub-title">How We Work</h3></div>
<div class="abs video">
  <div class="video-still" role="img" aria-label="Video still of business people in an office"></div>
  <svg width="288" height="202" viewBox="0 0 288 202">
    <polygon points="138,88 138,138 176,113" fill="#000"/>
    <line x1="10" y1="183" x2="278" y2="183" stroke="#111" stroke-width="1.5"/>
    <circle cx="26" cy="183" r="5" fill="#111"/>
  </svg>
</div>

<section class="abs whatwedo">
  <h3 class="sub-title">What We Do</h3>
  <p class="lead">Lorem ipsum dolor sit amet, consectetuer adipiscing elit. Nam cursus. Morbi ut mi.</p>
  <p class="small">Praesent mauris ante, elementum et, bibendum at, posuere sit amet, nibh. Duis tincidunt lectus quis dui viverra vestibulum. Suspendisse vulputate aliquam dui.</p>
  <p class="small gap">Nulla elementum dui ut augue. Aliquam vehicula mi at mauris. Maecenas placerat, nisl at consequat rhoncus, sem nunc gravida justo, quis eleifend arcu velit quis lacus. Donec convallis pede venenatis nibh.</p>
  <div class="learn">learn more</div>
</section>

<aside class="abs sidebar">
  <div class="side-head">User Login</div>
  <div class="login">
    <p class="note">To start connecting please log in first.<br>You can also create an account.</p>
    <div class="field-label">Username</div>
    <div class="field"></div>
    <div class="field-label">Password</div>
    <div class="field"></div>
    <div class="remember"><i></i>Remeber me</div>
    <div class="btn">Login</div>
  </div>
  <div class="side-head" style="margin-top:17px">Links to Blog</div>
  <ul class="blog-links">
    <li>Blog Link First</li>
    <li>Second Blog Link</li>
    <li>Blog Link Third</li>
    <li>Fourth Link</li>
    <li>Fifth Link of Blog</li>
    <li>Blog Fifth</li>
    <li>Sixth Link here</li>
    <li>Seventh link</li>
  </ul>
</aside>

<footer class="abs footer">
  <div class="foot-nav">Home<span>|</span>Features<span>|</span>Plugins<span>|</span>Tutorials<span>|</span>Fltcnsl<span>|</span>Contact</div>
  <div class="copy">© 2012 Company Name &nbsp;|&nbsp; All right reserved</div>
  <div class="social">
    <div class="social-item">Quabble<i></i></div>
    <div class="social-item">LM<i></i></div>
  </div>
</footer>

</body>
</html>
```